Vantage Forge needs a powerpoint design

We need a powerpoint design for an Information Technology based in Fairfax call "Vantage Forge". We are Information Technology solutions provider for the Federal Government. We develop Kestrel, Mobile and Cloud based solutions. We support the Healthcare and Financial sectors of the Government. We would like to see designs that use the colors of our logo. We've attached a copy of our logo. The final design should communicate Information Technology and System Integration with Agile Development.

Target Market(s)

Our target market is the Federal Government and System Integators in the Washington DC area.

Industry/Entity Type

Government

Requirements
Must have
• The powerpoint design must have a professional look.

```html
<!DOCTYPE html>
<html lang="en">
<head>
<meta charset="utf-8">
<title>Vantage Forge – Presentation Template</title>
<link rel="stylesheet" href="https://fonts.googleapis.com/css2?family=PT+Sans:wght@400;700&display=swap">
<style>
  :root{
    --canvas:#e6eaf0;
    --ink:#1c1c1c;
    --brand-blue:#1565b8;
    --brand-deep:#233a8f;
    --band-light:#2f86d6;
    --band-dark:#0b4f97;
    --accent-green:#8cc63f;
    --silver-top:#f3f3f3;
    --silver-mid:#c9c9c9;
    --white:#ffffff;
    --pie-main:#0f63b8;
    --pie-main-side:#0a4a8c;
    --pie-purple:#3b36a8;
    --pie-purple-side:#2a2680;
    --pie-violet:#5a4fd0;
    --pie-light:#1aa3e6;
  }
  *{box-sizing:border-box;margin:0;padding:0}
  html,body{width:1064px;height:1200px;overflow:hidden;background:var(--canvas)}
  body{position:relative;font-family:"PT Sans",Arial,sans-serif;color:var(--ink)}
  .slide{position:absolute;left:362px;width:482px;height:360px;overflow:hidden;box-shadow:0 2px 8px rgba(0,0,0,.35);background:var(--white)}
  .slide--title{top:148px;background:linear-gradient(180deg,var(--silver-top) 0%,var(--silver-mid) 22%,#e8e8e8 100%)}
  .slide--chart{top:724px}

  /* Title slide */
  .brand{position:absolute;left:0;right:0;display:flex;align-items:center;justify-content:center;gap:6px;font-weight:700;color:var(--brand-deep)}
  .brand__mark{width:16px;height:16px;background:var(--brand-deep)}
  .brand--hero{top:36px;font-size:15px}
  .title-band{position:absolute;left:0;top:0;width:482px;height:300px}
  .hero-title{position:absolute;top:150px;left:0;right:0;text-align:center;color:var(--white);font-size:27px;font-weight:700;letter-spacing:.5px}
  .hero-sub{position:absolute;top:189px;left:0;right:0;text-align:center;color:var(--accent-green);font-size:10.5px;font-weight:700}
  .hero-url{position:absolute;top:305px;left:0;right:0;text-align:center;font-size:8px;color:#333}
  .hero-copy{position:absolute;top:325px;left:0;right:0;text-align:center;font-size:7px;color:var(--brand-blue)}

  /* Chart slide */
  .chart-title{position:absolute;left:28px;top:28px;font-size:13px;font-weight:700;letter-spacing:.2px}
  .chart-rule{position:absolute;left:0;right:0;top:50px;height:2px;background:var(--band-light)}
  .chart-copy{position:absolute;left:62px;top:92px;width:152px;font-size:7.6px;line-height:10.2px;text-align:justify;color:#222}
  .chart-copy p+p{margin-top:10px}
  .pie{position:absolute;left:0;top:0}
  .legend{position:absolute;left:242px;top:265px;display:flex;gap:8px;font-size:6px;color:#333}
  .legend__item{display:flex;align-items:center;gap:2px}
  .legend__swatch{width:4px;height:4px}
  .footer{position:absolute;left:0;right:0;top:322px;height:26px;background:linear-gradient(90deg,var(--brand-deep),var(--brand-blue));color:var(--white);font-size:6.5px;display:flex;align-items:center}
  .footer__date{margin-left:46px}
  .footer__brand{margin-left:24px;display:flex;align-items:center;gap:4px;font-weight:700;font-size:9px}
  .footer__brand .brand__mark{width:10px;height:10px;background:var(--white)}
  .footer__url{margin-left:auto;margin-right:72px}
  .footer__num{position:absolute;right:0;top:-6px;width:56px;height:38px;background:var(--white);display:flex;align-items:center;justify-content:center}
  .footer__num span{width:24px;height:24px;background:var(--brand-deep);color:var(--white);font-size:7px;display:flex;align-items:center;justify-content:center}
</style>
</head>
<body>

<section class="slide slide--title">
  <svg class="title-band" viewBox="0 0 482 300" aria-hidden="true">
    <defs>
      <linearGradient id="band" x1="0" y1="0" x2="0" y2="1">
        <stop offset="0" stop-color="#1e74c8"/>
        <stop offset=".5" stop-color="var(--band-light)"/>
        <stop offset="1" stop-color="var(--band-dark)"/>
      </linearGradient>
    </defs>
    <path d="M0 78 H482 V280 C380 262 300 292 240 286 C170 280 90 262 0 282 Z" fill="url(#band)"/>
  </svg>
  <div class="brand brand--hero"><span class="brand__mark"></span>Vantage Forge</div>
  <h1 class="hero-title">PRESENTATION TITTLE HERE</h1>
  <p class="hero-sub">YOUR PRESENTATION SUB TITLE HERE</p>
  <p class="hero-url">www.vantageforgellc.com</p>
  <p class="hero-copy">© 2013 Vantage Forge. All rights reserved.</p>
</section>

<section class="slide slide--chart">
  <h2 class="chart-title">VANTAGE FORGE PIE CHART SAMPLE HERE</h2>
  <div class="chart-rule"></div>
  <div class="chart-copy">
    <p>The NRCF has forged a courageous and dynamic approach to the methodology of cancer research. By overcoming previous pitfalls that held the industry back, the NRCF has propelled the frontier of multiple myeloma research to a new level.</p>
    <p>Essential to this approach revious pitfalls that held the industry back, the NRCF has propelled the frontier of multiple myeloma research to a new level. are 4 groundbreaking initiatives that have revolutionized the way research and drug development are conducted. With these models, the NRCF can dramatically accelerate the pace at which lifesaving and new life-altering drugs can be brought to patients.</p>
  </div>
  <svg class="pie" width="482" height="360" viewBox="0 0 482 360" aria-label="3D pie chart">
    <path d="M232 165 A98 58 0 0 0 428 165 L428 183 A98 58 0 0 1 232 183 Z" fill="var(--pie-main-side)"/>
    <path d="M232 165 A98 58 0 0 0 245.1 194 L245.1 212 A98 58 0 0 1 232 183 Z" fill="var(--pie-purple-side)"/>
    <path d="M330 165 L330 107 A98 58 0 1 1 245.1 194 Z" fill="var(--pie-main)"/>
    <path d="M330 165 L245.1 194 A98 58 0 0 1 249.7 131.7 Z" fill="var(--pie-purple)"/>
    <path d="M330 165 L249.7 131.7 A98 58 0 0 1 296.5 110.5 Z" fill="var(--pie-violet)"/>
    <path d="M330 165 L296.5 110.5 A98 58 0 0 1 330 107 Z" fill="var(--pie-light)"/>
  </svg>
  <div class="legend">
    <span class="legend__item"><i class="legend__swatch" style="background:var(--pie-main)"></i>Pie Chart 1</span>
    <span class="legend__item"><i class="legend__swatch" style="background:var(--pie-purple)"></i>Pie Chart 2</span>
    <span class="legend__item"><i class="legend__swatch" style="background:var(--pie-violet)"></i>Pie Chart 3</span>
    <span class="legend__item"><i class="legend__swatch" style="background:var(--pie-light)"></i>Pie Chart 1</span>
  </div>
  <footer class="footer">
    <span class="footer__date">27/12/2013</span>
    <span class="footer__brand"><span class="brand__mark"></span>Vantage Forge</span>
    <span class="footer__url">www.vantageforgellc.com</span>
    <span class="footer__num"><span>11</span></span>
  </footer>
</section>

</body>
</html>
```